Meadowlark Seedhouse - New Strain Icons, Free seeds & delivery shipping icon and Discreet/Secure shippin

Hi guys - this is quite a big project and requires a full set of icons to be considered for completion. I've extended the project duration to 10 days to allow time for this.
We've just launched our mobile site and we're performing some clean ups of the images ready for a press launch.
Each image is required to be .png 50x50 - this is mandatory.
New Strain Icons - As you can see on each section on the homepage (screenshots provided below), there is an image for a strain. Looks very plain, we want it to have images/logos there that make it obvious that it's either for Bestseller, High Strength etc. - be creative and keep them all in theme with each other.
Free Seeds & Free Delivery - Part of our excellent customer satisfaction promise, we do different deals which offer customers some free seeds with their order. We also offer free shipping on orders at $99 or over! This information doesn't necessarily need to be on the image we just want the idea of free seeds and free delivery to stand out a SINGLE good image.
Underneath the Free Seeds & Free delivery section, there is going to be another section added about half the width of the sections already on there for our USPs of discreet shipping and secure shipping. We want two 50 x 50 images for this - I think maybe a ninja would be cool for the discreet shipping but it's your designs so be creative.
Like I said - it's a lot of work and I want it to be consistent all throughout the designs.

```html
<!DOCTYPE html>
<html lang="en">
<head>
<meta charset="utf-8">
<title>Meadowlark Seedhouse – Mobile Home</title>
<link href="https://fonts.googleapis.com/css2?family=PT+Sans+Narrow:wght@400;700&display=swap" rel="stylesheet">
<style>
  :root {
    --page-bg: #e9e9e7;
    --strength: #b84a8e;
    --autos: #5b4d92;
    --banks: #3f8dcc;
    --free: #3c3c3c;
    --footer: #5b5b5b;
    --action: #6dca0b;
    --action-text: #1f3a06;
    --footer-head: #7fd01c;
    --white: #ffffff;
    --tile: #ececec;
    --tile-text: #3a3a3a;
  }
  * { margin: 0; padding: 0; box-sizing: border-box; }
  html, body {
    width: 1200px; height: 3858px; overflow: hidden;
    background: var(--page-bg);
    font-family: "PT Sans Narrow", "Arial Narrow", sans-serif;
    color: var(--white);
  }
  .page { position: relative; width: 1200px; height: 3858px; overflow: hidden; }
  .section { position: absolute; left: 0; width: 1200px; overflow: hidden; }
  .section-title {
    position: absolute; left: 66px; font-size: 90px; font-weight: 400;
    line-height: 90px; white-space: nowrap;
  }
  .section-text { position: absolute; left: 66px; font-size: 48px; line-height: 66px; }
  .action-button {
    position: absolute; left: 66px; height: 156px;
    background: var(--action); color: var(--action-text);
    border-radius: 8px; font-size: 54px; text-decoration: none;
    display: flex; align-items: center; justify-content: center;
  }
  .art { position: absolute; border-radius: 18px; }

  .strength { top: 90px; height: 600px; background: var(--strength); }
  .strength .section-title { top: 99px; }
  .strength .section-text { top: 258px; }
  .strength .action-button { top: 375px; width: 696px; }
  .strength .art { left: 825px; top: 120px; width: 315px; height: 270px;
    background: linear-gradient(135deg, #8fd34a, #d9e3cf); }

  .autos { top: 720px; height: 681px; background: var(--autos); }
  .autos .section-title { top: 111px; }
  .autos .section-text { top: 267px; line-height: 63px; }
  .autos .action-button { top: 453px; width: 696px; }
  .autos .art { left: 825px; top: 150px; width: 315px; height: 330px;
    background: radial-gradient(circle, #f1f1ef 45%, #c9c6d6); }

  .banks { top: 1440px; height: 996px; background: var(--banks); }
  .banks-title {
    position: absolute; top: 57px; width: 100%; text-align: center;
    font-size: 72px; font-weight: 400; line-height: 72px;
  }
  .bank { position: absolute; width: 315px; }
  .bank-tile {
    height: 204px; background: var(--tile); border-radius: 6px;
    display: flex; align-items: center; justify-content: center; text-align: center;
    color: var(--tile-text); font-size: 36px; font-weight: 700; padding: 0 18px; line-height: 1.1;
  }
  .bank-name { margin-top: 19px; font-size: 48px; line-height: 63px; }

  .free { top: 2475px; height: 660px; background: var(--free); }
  .free .section-title { top: 96px; }
  .free .section-text { top: 258px; font-size: 54px; }
  .free .action-button { top: 441px; width: 1071px; }
  .free .art { left: 864px; top: 60px; width: 276px; height: 180px;
    background: linear-gradient(135deg, #7ac943, #5aa532); }

  .footer { top: 3174px; height: 684px; background: var(--footer); }
  .footer-col { position: absolute; top: 45px; }
  .footer-head { font-size: 54px; color: var(--footer-head); line-height: 54px; height: 97px; }
  .footer-link { display: block; font-size: 57px; line-height: 105px; color: var(--white); text-decoration: none; }
</style>
</head>
<body>
<main class="page">

  <section class="section strength">
    <h2 class="section-title">High Strength</h2>
    <p class="section-text">Super High THC Seeds , 15% THC+</p>
    <a class="action-button">Buy High THC seeds</a>
    <div class="art" role="img" aria-label="Green molecule illustration for high strength strains"></div>
  </section>

  <section class="section autos">
    <h2 class="section-title">Big Yield Autos</h2>
    <p class="section-text">Well over 1500 + Auto flowering<br>High Yielders</p>
    <a class="action-button">Buy High Yield Autos</a>
    <div class="art" role="img" aria-label="Gear illustration with green leaves and flowers for high yield autoflowering strains"></div>
  </section>

  <section class="section banks">
    <h2 class="banks-title">TOP SEED BANKS</h2>
    <div class="bank" style="left:66px;top:165px"><div class="bank-tile">Northfield Female Seeds</div><p class="bank-name">Northfield Female Seeds</p></div>
    <div class="bank" style="left:444px;top:165px"><div class="bank-tile">Greenleaf Feminised</div><p class="bank-name">Greenleaf Feminised</p></div>
    <div class="bank" style="left:822px;top:165px"><div class="bank-tile">Top of the Field</div><p class="bank-name">Top of the Field</p></div>
    <div class="bank" style="left:66px;top:576px"><div class="bank-tile">Hollis Farm</div><p class="bank-name">Hollis Farm</p></div>
    <div class="bank" style="left:444px;top:576px"><div class="bank-tile">Dr Bramwell</div><p class="bank-name">Dr Bramwell</p></div>
    <div class="bank" style="left:822px;top:576px"><div class="bank-tile">Quick Sprouts</div><p class="bank-name">Quick Sprouts</p></div>
  </section>

  <section class="section free">
    <h2 class="section-title">Free Seeds &amp; Delivery</h2>
    <p class="section-text">Our free seeds are exclusive, branded and sought<br>after.</p>
    <a class="action-button">View Free Seed Deals</a>
    <div class="art" role="img" aria-label="Green delivery truck carrying a gift bow for free seeds and delivery"></div>
  </section>

  <footer class="section footer">
    <div class="footer-col" style="left:36px">
      <p class="footer-head">SUPPORT</p>
      <a class="footer-link">Track your order</a>
      <a class="footer-link">Delivery times</a>
      <a class="footer-link">Shipping information</a>
      <a class="footer-link">Returns</a>
    </div>
    <div class="footer-col" style="left:636px">
      <p class="footer-head">USEFUL INFORMATION</p>
      <a class="footer-link">Privacy policy</a>
      <a class="footer-link">Payment methods</a>
      <a class="footer-link">FAQs</a>
      <a class="footer-link">Disclaimer</a>
    </div>
  </footer>

</main>
</body>
</html>
```